An anniversary gift for my girlfriend

My girlfriend and I have been dating for almost 2 years. We met online and this has afforded us the really unique opportunity to have the first words we said to each other (the whole conversation, in fact) preserved. We're moving in together in a few months and she doesn't know that I saved the conversation. I've been waiting for this to turn it into something we can hang in our new place.

The only phrase I want to use is:
"Well if you dislike people's knees then I think we'll get along famously"

It's an Nobody Leaves Before Midnight in Portland reference for the curious.

I want the poster to use the words themselves as the art; I'm thinking typography. I'd like it to match her aesthetic, she likes to wear Nora Vell and T. Brisk. Colors shouldn't be anything too "girly". Somewhere I'd like to include the date June 1, 2015. It shouldn't be a major piece of the poster though, just a way to denote the date.

It should fit (and be fully visible in) a 16x20 (inches) frame

Thanks in advance for the work!

Requirements
Must have
• Must use only the words: "Well if you dislike people's knees then I think we'll get along famously"
• I want this to be typography, so making the phrase the center of the poster and the art itself.

```html
<!DOCTYPE html>
<html lang="en">
<head>
<meta charset="utf-8">
<title>Well if you dislike people's knees</title>
<link rel="stylesheet" href="https://fonts.googleapis.com/css2?family=Old+Standard+TT:wght@400;700&family=Sorts+Mill+Goudy:ital@1&family=Questrial&display=swap">
<style>
  :root {
    --paper: #fdf283;
    --ink: #111111;
  }
  html, body {
    margin: 0;
    padding: 0;
    width: 848px;
    height: 1200px;
    overflow: hidden;
    background: var(--paper);
  }
  .poster {
    display: block;
    width: 848px;
    height: 1200px;
  }
  .poster__frame {
    fill: none;
    stroke: var(--ink);
    stroke-width: 1.5;
  }
  .quote text { fill: var(--ink); }
  .quote__serif {
    font-family: "Old Standard TT", "Times New Roman", serif;
    font-weight: 400;
  }
  .quote__serif--bold {
    font-family: "Old Standard TT", "Times New Roman", serif;
    font-weight: 700;
  }
  .quote__italic {
    font-family: "Sorts Mill Goudy", "Georgia", serif;
    font-style: italic;
  }
  .quote__sans {
    font-family: "Questrial", "Century Gothic", sans-serif;
  }
  .poster__date {
    font-family: "Questrial", "Century Gothic", sans-serif;
    font-size: 14px;
    fill: var(--ink);
  }
</style>
</head>
<body>
<svg class="poster" viewBox="0 0 848 1200" xmlns="http://www.w3.org/2000/svg">
  <rect class="poster__frame" x="18.5" y="18.5" width="811" height="1163"/>

  <g class="quote">
    <text class="quote__serif" x="45" y="395" font-size="190" textLength="422" lengthAdjust="spacingAndGlyphs">“Well</text>
    <text class="quote__serif" x="480" y="380" font-size="82" textLength="266" lengthAdjust="spacingAndGlyphs">if you</text>
    <text class="quote__sans" x="228" y="470" font-size="66" textLength="542" lengthAdjust="spacingAndGlyphs">dislike people’s</text>
    <text class="quote__italic" x="150" y="558" font-size="128" textLength="350" lengthAdjust="spacingAndGlyphs">knees</text>
    <text class="quote__serif" x="275" y="652" font-size="86" textLength="500" lengthAdjust="spacingAndGlyphs">then I think</text>
    <text class="quote__sans" x="105" y="750" font-size="84" textLength="685" lengthAdjust="spacingAndGlyphs">we’ll get along</text>
    <text class="quote__serif--bold" x="158" y="838" font-size="108" textLength="628" lengthAdjust="spacingAndGlyphs">famously”</text>
  </g>

  <text class="poster__date" x="508" y="867">June 1, 2015</text>
</svg>
</body>
</html>
```